1 Page Sales Brochure of our Services

I need to create a one page brochure that our sales team can take into meetings about our services - Need this to be an impressive one page that looks fresh and new using our brand colors of Vantora green, black and white. Our brand looks "clean" think Quenly brand in how everything is clean and white and crisp. Our website showcases our services: https://vantorasports.com/services/ --- After done with this project I would like to create a full booklet. Want to begin with this project first.

Target Market(s)

State of Texas

Industry/Entity Type

Sports Construction in Texas Only

Font styles to use
Serif

Colors
00AB8E
00BBA5
67D7C9
C6EFE9
E9F9F6

Requirements
Must have
• Front and Back and cover our services outlined on our website: https://vantorasports.com/services/
Nice to have
• Need one that can get sent digital and printed -- Our colors are the Vantora green, white and black - We want brochure to look clean, almost like the Quenly feel of their product's branding

```html
<!DOCTYPE html>
<html lang="en">
<head>
<meta charset="utf-8">
<title>Vantora Sports Construction – Services Brochure</title>
<link rel="stylesheet" href="https://fonts.googleapis.com/css2?family=Oswald:wght@500&family=Montserrat:wght@400;500;600;700&display=swap">
<style>
:root{
  --green:#1f7a36;
  --green-deep:#17622b;
  --green-band:rgba(25,100,45,.88);
  --charcoal:#3b3b3d;
  --ink:#222;
  --white:#fff;
  --stage:#e8ecec;
}
*{margin:0;padding:0;box-sizing:border-box}
html,body{width:1050px;height:1200px;overflow:hidden;background:var(--stage)}
body{font-family:"Montserrat",Arial,sans-serif;color:var(--ink);position:relative}
.page{position:absolute;top:247px;width:500px;height:706px;background:var(--white);overflow:hidden;box-shadow:0 2px 10px rgba(0,0,0,.15)}
.page--front{left:15px}
.page--back{left:535px}
.abs{position:absolute}
.photo{position:absolute}
.heading{font-family:"Oswald","Arial Narrow",sans-serif;font-weight:500;text-transform:uppercase;letter-spacing:.2px}
.body-copy{font-size:7.4px;line-height:1.32;text-align:justify}
.body-copy p+p{margin-top:6px}
.caption{position:absolute;color:var(--white);font-weight:600;font-size:9.5px;letter-spacing:.3px;padding-left:20px;display:flex;align-items:center}
.brand-name{left:20px;top:22px;font-size:36px;font-weight:600;color:var(--green);display:flex;align-items:center;gap:8px;letter-spacing:-.5px}
.brand-name .mark{width:12px;height:12px;background:var(--green)}
.services-title{left:19px;top:110px;font-size:20px;color:var(--ink)}
.services-sub{left:19px;top:142px;font-size:9.6px;font-weight:700;color:var(--green);line-height:1.25}
.services-intro{left:19px;top:176px;width:462px}
.services-intro .wrap{float:right;width:244px;height:29px}
.services-box{left:0;top:253px;width:211px;height:234px;background:var(--green)}
.services-box .frame{position:absolute;left:10px;top:10px;right:0;bottom:0;border-left:1px solid rgba(255,255,255,.8);border-top:1px solid rgba(255,255,255,.8)}
.services-box h3{position:absolute;left:19px;top:20px;color:var(--white);font-size:17px}
.services-box ul{position:absolute;left:30px;top:55px;list-style:none;color:var(--white);font-size:9.6px;font-weight:500}
.services-box li{margin-bottom:7.2px}
.services-box li::before{content:"• ";font-size:8px}
.track-copy{left:240px;top:423px;width:246px}
.grass-copy{left:19px;top:627px;width:462px}
.rule{position:absolute;bottom:0;height:6px}
.stadium-band{left:0;top:135px;width:500px;height:77px;background:var(--green-band);color:var(--white);padding:10px 15px}
.stadium-band h3{font-size:9.6px;font-weight:600;letter-spacing:.3px;margin-bottom:6px}
.stadium-band p{font-size:7.4px;line-height:1.3;text-align:justify}
.synthetic-col{left:0;top:212px;width:151px;height:385px;background:var(--charcoal);color:var(--white);padding:8px 10px}
.synthetic-col h2{font-size:17px;line-height:1.35;margin-bottom:8px}
.synthetic-col h4{font-size:9.6px;font-weight:600;line-height:1.3;margin-bottom:8px}
.synthetic-col p{font-size:7.2px;line-height:1.3;margin-bottom:8px}
.contact{left:0;top:597px;width:151px;height:103px;background:var(--green);color:var(--white);padding:20px 11px}
.contact .phone{font-size:14.5px;font-weight:500;margin-bottom:9px}
.contact .line{font-size:7.6px;font-weight:600;line-height:1.4}
.contact .mail{margin-bottom:8px}
.right-col{left:170px;top:220px;width:316px}
.right-col h3{font-size:9.6px;font-weight:700;color:var(--green);margin:0 0 5px;letter-spacing:.2px}
.right-col .body-copy{margin-bottom:8px}
.right-col strong{color:var(--green);font-weight:700}
.maint-list{list-style:none;font-size:7.2px;line-height:1.55}
.maint-list b{color:var(--green);font-weight:600}
.thumbs{left:157px;top:640px;display:flex;gap:3px}
.thumbs div{width:66.4px;height:54px}
</style>
</head>
<body>

<section class="page page--front">
  <div class="abs brand-name"><span class="mark"></span>Vantora</div>

  <svg class="photo" style="left:0;top:0" width="500" height="200" viewBox="0 0 500 200">
    <defs>
      <linearGradient id="siteGrad" x1="0" y1="0" x2="0" y2="1">
        <stop offset="0" stop-color="#8fa8b8"/>
        <stop offset=".35" stop-color="#a6a58a"/>
        <stop offset="1" stop-color="#c4b9a2"/>
      </linearGradient>
    </defs>
    <polygon points="234,13 500,13 500,192 253,192" fill="url(#siteGrad)" role="img" aria-label="Aerial photo of a stadium construction site with graded earth"/>
    <line x1="220" y1="0" x2="253" y2="192" stroke="#222" stroke-width="1"/>
    <polygon points="227,83 233,83 257,172 251,172" fill="var(--green)"/>
  </svg>

  <h2 class="abs heading services-title">Services</h2>
  <div class="abs services-sub">TURNKEY SOLUTIONS FOR<br>SPORTS CONSTRUCTION</div>
  <div class="abs body-copy services-intro">
    <span class="wrap"></span>Vantora Sports Construction offers turnkey solutions in the realm of general sports construction. We're committed to excellence in all we do, and we seek to develop lasting relationships with our clients. Vantora is not in the business to win a single job and move on. We are working to earn your trust and business as we want you as a customer for life. At Vantora we have 7 Proverbs we strive to live by. Our #1 proverb is to "Deliver On Our Promises". That is our promise to you that we will strive to deliver on time with the quality and service you expect and deserve on every job.
  </div>

  <div class="abs services-box">
    <div class="frame"></div>
    <h3 class="heading">Our Services Include:</h3>
    <ul>
      <li>Track Construction</li>
      <li>Natural Grass Fields</li>
      <li>Synthetic Field Construction</li>
      <li>Stadium Construction</li>
      <li>Tennis Court Construction</li>
      <li>Service + Maintenance</li>
      <li>Stadium Lighting</li>
      <li>Surface Maintenance + Repair</li>
    </ul>
  </div>

  <div class="photo" style="left:218px;top:253px;width:282px;height:150px;background:linear-gradient(160deg,#c9ccce 0%,#5aa04a 30%,#3f8a3a 70%,#7b3b36 100%)" role="img" aria-label="Aerial photo of a synthetic football field surrounded by a running track"></div>
  <div class="caption" style="left:218px;top:387px;width:282px;height:20px;background:var(--green)">TRACK CONSTRUCTION</div>

  <div class="abs body-copy track-copy">
    <p>When you're looking to have a track installed at your school or facility, there are many factors that come into play. This is a highly specialized job, and you'll want to work with a team that has the expertise necessary to plan and execute a quality installation. At Vantora, we are proud to offer solutions in track construction for a variety of client types.</p>
    <p>Vantora recommends the Stridelon line of running track systems developed by Korvane, owned by Fieldmark Group, as the industry leaders in high quality, performance-enhancing systems that result in unmatched results for the lifecycle of your track.</p>
    <p>Our track specialists install base mats to full pour systems with custom color options. One of the most popular new features to track systems is alternating exchange zone colors to really make your track stand out. Vantora has chosen to partner with Korvane for our track products as we believe they provide the highest quality product on the market today with the most durable and high performing track systems.</p>
  </div>

  <div class="photo" style="left:0;top:487px;width:227px;height:131px;background:linear-gradient(180deg,#a9cde3 0%,#cfe0ea 35%,#6f9a4a 50%,#4f8a2e 100%)" role="img" aria-label="Photo of a natural grass baseball field under a clear sky"></div>
  <div class="caption" style="left:0;top:600px;width:227px;height:18px;background:var(--charcoal)">NATURAL GRASS FIELDS</div>

  <div class="abs body-copy grass-copy">
    Natural Grass is a growing area of our business and we have brought in natural grass experts to join the Vantora team who understand the challenges involved with installing and maintaining grass fields. Two of our experts are certified field builders with one specializing in both synthetic and natural grass installations. Our team operates with specialized equipment allowing massive amounts of dirt to be moved and graded when building natural grass fields. Due to the specialists on our team, we can assist in the design build of your water system to ensure your natural grass will hold the test of time after our installation is complete. If a natural grass field makes the most sense for your specific venue and application, Vantora can help you to bring that project to life.
  </div>

  <div class="rule" style="left:0;width:304px;background:var(--green)"></div>
  <div class="rule" style="left:307px;width:193px;background:var(--charcoal)"></div>
</section>

<section class="page page--back">
  <div class="photo" style="left:0;top:0;width:500px;height:212px;background:linear-gradient(170deg,#e3e6e8 0%,#aab2b8 30%,#5fa14c 55%,#3f8a37 75%,#8a5a48 100%)" role="img" aria-label="Aerial photo of a football stadium with a synthetic turf field"></div>
  <svg class="abs" style="left:0;top:0" width="500" height="212" viewBox="0 0 500 212">
    <polygon points="385,0 430,0 430,135 385,135" fill="rgba(60,60,60,.28)"/>
    <polygon points="120,120 250,0 300,0 170,135" fill="rgba(30,110,50,.35)"/>
    <line x1="440" y1="60" x2="433" y2="135" stroke="#3b3b3d" stroke-width="2"/>
  </svg>
  <div class="abs stadium-band">
    <h3>STADIUM CONSTRUCTION</h3>
    <p>In every sense of the word, Vantora is a one-stop shop for all things sports construction. We are a true turn-key construction company owned and operated by seasoned professionals who care. From ground-up stadium construction to total lifecycle planning, we provide custom construction solutions through all stages of your projects.</p>
  </div>
  <svg class="abs" style="left:0;top:205px" width="500" height="30" viewBox="0 0 500 30">
    <line x1="437" y1="0" x2="431" y2="22" stroke="#3b3b3d" stroke-width="1.5"/>
  </svg>

  <div class="abs synthetic-col">
    <h2 class="heading">Synthetic Field<br>Construction</h2>
    <h4>The Right VerdaTurf System for Every Venue</h4>
    <p>With the wide selection of synthetic turf systems– no matter the venue or sport– Vantora has a viable solution.</p>
    <p>VerdaTurf's premium turf system series boasts heavy face weights for the best the industry has to offer in aesthetics, durability, and player protection. These systems are driven by the latest research, and technology pushing the industry towards the most grass-like surfaces available.</p>
    <p>Our sales team will be able to evaluate your system needs and preferences and help to identify the best system for your specific application. We have become experts in the industry with over 12 years of experience in sports construction. The most important component to understand is that you are not simply purchasing "turf." You are purchasing a turf system. There are multiple components to properly build a turf system which require a great amount of expertise.</p>
  </div>

  <div class="abs contact">
    <div class="phone">(512) 555 0148</div>
    <div class="line mail">info@vantorasports.com</div>
    <div class="line">418 East Cedar Street<br>Lufkin, Texas 75901</div>
  </div>

  <div class="abs right-col">
    <h3>TENNIS COURT CONSTRUCTION</h3>
    <div class="body-copy">To ensure that our customers are playing on the best tennis courts available, we've partnered with Korvane to provide Courtline court surfacing systems. Courtline offers a variety of impact reducing, performance enhancing court systems that are of the highest quality in the industry.</div>
    <h3>SERVICE + MAINTENANCE</h3>
    <div class="body-copy">Vantora Sports is here to support you throughout the entire lifecycle of your sports construction projects from conception to intermittent servicing when needed. We provide maintenance services and support for all sports surfaces, helping you protect your investment and extend the life of your synthetic turf, track or tennis court through education, performance testing, and maintenance services. It's important to us that each customer gets the most out of their sports surfaces. Call us today at <strong>512-555-0148</strong> to speak with one of our maintenance experts. We would love to take care of you.</div>
    <h3>STADIUM LIGHTING</h3>
    <div class="body-copy">Vantora also provides lighting services. Take advantage of the energy efficiency and cost savings by converting to LED lighting. According to the US Department of Energy, light-emitting diodes (LED) are six to seven times more energy efficient than conventional light bulbs and cut energy use by more than 80 percent. LED light bulbs can also last 25,000 hours or more, which is 25 times longer than traditional bulbs. You can see why LED lighting makes financial sense!</div>
    <h3>SURFACE MAINTENANCE + REPAIR</h3>
    <div class="body-copy">All sports systems involve some component of maintenance to ensure your surface is performing properly and will withstand the test of time. Many of our synthetic fields undergo annual field maintenance and bacterial and COVID killing sprays. This is particularly important for athletes who will be using indoor facilities as they do not receive sunlight which aids in killing bacteria. If you would like to have a free maintenance or field/surface evaluation, please email us at <strong>aftercare@vantorasports.com.</strong></div>
    <h3>SPORTS SURFACE MAINTENANCE INCLUDES:</h3>
    <ul class="maint-list">
      <li><b>COVID + Bacterial Killer Sprays:</b> Antimicrobial Treatments</li>
      <li><b>Turf Repairs:</b> Seams, Inlays</li>
      <li><b>Grooming:</b> Sweeping, Infill Top Dressing</li>
      <li><b>Performance Testing:</b> Field Longevity Testing, Safety Testing, Impact Testing</li>
    </ul>
  </div>

  <div class="abs thumbs">
    <div style="background:linear-gradient(180deg,#bcd5e6,#3b72b5)" role="img" aria-label="Photo of a blue tennis court"></div>
    <div style="background:linear-gradient(180deg,#d8dde0,#3f8a37)" role="img" aria-label="Photo of a technician repairing turf seams"></div>
    <div style="background:linear-gradient(90deg,#6f8c5a,#4c7a3c)" role="img" aria-label="Before photo of an indoor turf field"></div>
    <div style="background:linear-gradient(90deg,#4c8d3c,#67b24d)" role="img" aria-label="After photo of an indoor turf field"></div>
    <div style="background:linear-gradient(180deg,#c5d8e6,#6a4a9a)" role="img" aria-label="Photo of a grooming machine on a purple and green field"></div>
  </div>

  <div class="rule" style="left:0;width:278px;background:var(--green)"></div>
  <div class="rule" style="left:281px;width:219px;background:var(--charcoal)"></div>
</section>

</body>
</html>
```